Financial Research Company Brand Ad

We need a poster design for "Varnholt Analytics" 254mm(h) x 190mm (w) Our research focuses on banks, bank credit, liquidity & corporate solvency. Our believes "Get the credit & liquidity trends right & the rest follows" Please see our website for more information. www.varnholt-analytics.example

Industry/Entity Type

Bank

```html
<!DOCTYPE html>
<html lang="en">
<head>
<meta charset="utf-8">
<title>Varnholt Analytics – Credit &amp; Liquidity Poster</title>
<link rel="stylesheet" href="https://fonts.googleapis.com/css2?family=Archivo+Black&family=Arimo:wght@700&display=swap">
<style>
  :root {
    --navy-deep: #211d5c;
    --navy-mid: #3a3575;
    --lavender: #9d98bd;
    --paper: #ffffff;
    --ink: #1c1a1a;
    --arrow-blue: #2b3b9b;
    --frame: #2a2a2a;
  }
  html, body {
    margin: 0;
    padding: 0;
    width: 899px;
    height: 1200px;
    overflow: hidden;
    background: var(--paper);
  }
  .poster {
    position: relative;
    width: 899px;
    height: 1200px;
    background: var(--paper);
  }
  .poster__frame {
    position: absolute;
    left: 6px;
    top: 6px;
    width: 885px;
    height: 1185px;
    border: 1.5px solid var(--frame);
    box-sizing: border-box;
    overflow: hidden;
  }
  .chart {
    position: absolute;
    left: 0;
    top: 0;
    width: 885px;
    height: 860px;
    display: block;
  }
  .label {
    position: absolute;
    margin: 0;
    font-family: "Archivo Black", "Arial Black", sans-serif;
    letter-spacing: 1px;
    line-height: 1;
  }
  .label--target {
    color: var(--paper);
    font-size: 44px;
    text-shadow: 0 0 10px rgba(255,255,255,0.55);
  }
  .label--source {
    color: var(--ink);
    font-size: 37px;
  }
  .label--solvency { left: 168px; top: 76px; }
  .label--value { left: 634px; top: 76px; }
  .label--liquidity { left: 40px; top: 846px; }
  .label--credit { left: 418px; top: 846px; }
  .motto {
    position: absolute;
    left: 14px;
    top: 932px;
    margin: 0;
    font-family: "Arimo", Arial, sans-serif;
    font-weight: 700;
    font-size: 41px;
    line-height: 54px;
    color: var(--ink);
  }
  .motto__line { display: block; }
  .motto__line--indent { padding-left: 24px; }
  .brand {
    position: absolute;
    left: 520px;
    top: 1048px;
    display: flex;
    align-items: center;
    gap: 14px;
  }
  .brand__dot {
    width: 72px;
    height: 72px;
    border-radius: 50%;
    background: var(--arrow-blue);
  }
  .brand__name {
    font-family: "Arimo", Arial, sans-serif;
    font-weight: 700;
    font-size: 25px;
    color: var(--ink);
  }
</style>
</head>
<body>
<main class="poster">
  <div class="poster__frame">
    <svg class="chart" viewBox="0 0 885 860" xmlns="http://www.w3.org/2000/svg" aria-hidden="true">
      <defs>
        <linearGradient id="backdrop" x1="0" y1="0" x2="0" y2="860" gradientUnits="userSpaceOnUse">
          <stop offset="0" stop-color="var(--navy-deep)"/>
          <stop offset="0.42" stop-color="var(--navy-deep)"/>
          <stop offset="0.62" stop-color="var(--navy-mid)"/>
          <stop offset="0.8" stop-color="var(--lavender)"/>
          <stop offset="0.96" stop-color="var(--paper)"/>
        </linearGradient>
        <pattern id="grid" width="68" height="68" patternUnits="userSpaceOnUse" x="-6" y="-8">
          <path d="M68 0 V68 M0 68 H68" fill="none" stroke="#ffffff" stroke-width="2.5"/>
        </pattern>
        <linearGradient id="gridFade" x1="0" y1="0" x2="0" y2="860" gradientUnits="userSpaceOnUse">
          <stop offset="0.84" stop-color="#ffffff" stop-opacity="0"/>
          <stop offset="0.96" stop-color="#ffffff" stop-opacity="1"/>
        </linearGradient>
        <linearGradient id="arrowFill" x1="0" y1="0" x2="0" y2="840" gradientUnits="userSpaceOnUse">
          <stop offset="0" stop-color="var(--arrow-blue)"/>
          <stop offset="0.82" stop-color="var(--arrow-blue)"/>
          <stop offset="1" stop-color="var(--arrow-blue)" stop-opacity="0"/>
        </linearGradient>
        <filter id="glow" x="-30%" y="-10%" width="160%" height="120%">
          <feMorphology in="SourceAlpha" operator="dilate" radius="3" result="grow"/>
          <feGaussianBlur in="grow" stdDeviation="6" result="blur"/>
          <feFlood flood-color="#ffffff" flood-opacity="0.9"/>
          <feComposite in2="blur" operator="in" result="halo"/>
          <feMerge><feMergeNode in="halo"/><feMergeNode in="SourceGraphic"/></feMerge>
        </filter>
      </defs>
      <rect class="chart__backdrop" width="885" height="860" fill="url(#backdrop)"/>
      <rect class="chart__grid" width="885" height="860" fill="url(#grid)"/>
      <rect class="chart__fade" width="885" height="860" fill="url(#gridFade)"/>
      <polygon class="chart__arrow chart__arrow--solvency" filter="url(#glow)" fill="url(#arrowFill)"
        points="126,836 224,219 206,210 293,121 344,246 322,240 229,836"/>
      <polygon class="chart__arrow chart__arrow--value" filter="url(#glow)" fill="url(#arrowFill)"
        points="540,836 636,270 617,260 702,157 751,284 731,279 643,836"/>
    </svg>

    <h2 class="label label--target label--solvency">SOLVENCY</h2>
    <h2 class="label label--target label--value">VALUE</h2>
    <h2 class="label label--source label--liquidity">LIQUIDITY</h2>
    <h2 class="label label--source label--credit">CREDIT LINES</h2>

    <p class="motto">
      <span class="motto__line">“Get the credit &amp; liquidity trends right</span>
      <span class="motto__line motto__line--indent">&amp; the rest follows”</span>
    </p>

    <div class="brand">
      <span class="brand__dot"></span>
      <span class="brand__name">Varnholt Analytics</span>
    </div>
  </div>
</main>
</body>
</html>
```